Where's my Gym Buddy? looking to do two promotions as listed in project description

looking for two designs.

1: selfie frame design!! (wording) Frost Grind Carnival, my Summer fitness has started, Tag a friend who should be joining me. T.C Tag your posts to @brightloopsydney to win points for the competition. (Snow graphic) in a selfie frame design. this needs to be the same design but across different departments as seen at the top of the photo's I've attached EG: #brightloopfitness #brightloopindoor #brightloopswim #brightloopwyong

2: Selfie Frame Design!! (Wording) Where's my gym buddy?, Tag a friend who should be at the gym, T.C.Tag your posts to @brightloopsydney to win points for the competition. Spot the Pilot Feel Selfie frame design

Target Market(s)

Gym Members

Industry/Entity Type

Gym

Colors

Designer to choose colors to be used in the design.

Requirements
Must have
• quirky and funky design, must include wording listed, must be a selfie frame design
Should not have
• whilst we are a big corporate gym, we pride ourselves on having really funky advertisements, so please no boring business corporate typical designs

```html
<!DOCTYPE html>
<html lang="en">
<head>
<meta charset="utf-8">
<title>Frost Grind Carnival – Selfie Frame</title>
<link rel="stylesheet" href="https://fonts.googleapis.com/css2?family=Baloo+2:wght@800&family=Share+Tech+Mono&family=Electrolize&display=swap">
<style>
  :root {
    --ice-blue: #2e80ab;
    --ice-blue-light: #4a9cc6;
    --ice-blue-deep: #226b93;
    --festival-red: #e83f34;
    --snow-white: #ffffff;
    --frame-shadow: rgba(0, 0, 0, 0.35);
  }
  * { margin: 0; padding: 0; box-sizing: border-box; }
  html, body {
    width: 848px;
    height: 1200px;
    overflow: hidden;
    background: var(--ice-blue);
  }
  .selfie-frame {
    position: relative;
    width: 848px;
    height: 1200px;
    overflow: hidden;
  }
  .snow-backdrop {
    position: absolute;
    inset: 0;
    background:
      radial-gradient(ellipse at 50% 0%, rgba(255,255,255,0.55) 0%, rgba(255,255,255,0) 22%),
      radial-gradient(ellipse at 50% 100%, rgba(255,255,255,0.45) 0%, rgba(255,255,255,0) 18%),
      linear-gradient(180deg, var(--ice-blue-light) 0%, var(--ice-blue) 30%, var(--ice-blue) 75%, var(--ice-blue-deep) 100%);
  }
  .festival-title {
    position: absolute;
    top: 58px;
    left: 0;
    width: 848px;
    text-align: center;
    font-family: "Baloo 2", "Arial Black", sans-serif;
    font-weight: 800;
    font-style: italic;
    font-size: 80px;
    line-height: 1;
    letter-spacing: -1px;
    color: var(--festival-red);
    -webkit-text-stroke: 0;
    paint-order: stroke fill;
    text-shadow:
      0 0 0 var(--snow-white),
      -5px -5px 0 var(--snow-white), 5px -5px 0 var(--snow-white),
      -5px 5px 0 var(--snow-white), 5px 5px 0 var(--snow-white),
      0 -6px 0 var(--snow-white), 0 6px 0 var(--snow-white),
      -6px 0 0 var(--snow-white), 6px 0 0 var(--snow-white),
      4px 10px 8px rgba(0,0,0,0.35);
    transform: skewX(-6deg);
  }
  .slogan-band {
    position: absolute;
    top: 192px;
    left: 0;
    width: 848px;
    height: 60px;
    background: var(--festival-red);
    color: var(--snow-white);
    font-family: "Electrolize", sans-serif;
    font-size: 43px;
    line-height: 60px;
    text-align: center;
    letter-spacing: 2px;
    text-transform: uppercase;
  }
  .photo-window {
    position: absolute;
    left: 102px;
    top: 302px;
    width: 649px;
    height: 657px;
    background: var(--snow-white);
    transform: rotate(4.1deg);
    box-shadow: 0 0 0 6px var(--snow-white), 0 4px 10px var(--frame-shadow), inset 0 0 12px rgba(0,0,0,0.35);
  }
  .tag-friend-band {
    position: absolute;
    top: 1013px;
    left: 0;
    width: 848px;
    height: 62px;
    background: var(--snow-white);
    color: var(--festival-red);
    font-family: "Share Tech Mono", monospace;
    font-size: 35px;
    line-height: 62px;
    text-align: center;
    letter-spacing: 2px;
  }
  .terms-band {
    position: absolute;
    top: 1085px;
    left: 0;
    width: 848px;
    height: 98px;
    background: var(--festival-red);
    color: var(--snow-white);
    font-family: "Share Tech Mono", monospace;
    font-size: 35px;
    line-height: 40px;
    text-align: center;
    letter-spacing: 2px;
    padding-top: 9px;
  }
</style>
</head>
<body>
  <main class="selfie-frame">
    <div class="snow-backdrop" role="img" aria-label="Icy blue backdrop scattered with snowflakes and falling snow"></div>
    <h1 class="festival-title">Frost Grind Carnival</h1>
    <p class="slogan-band">My Summer Fitness Has Started</p>
    <div class="photo-window" aria-label="Selfie photo area"></div>
    <p class="tag-friend-band">Tag a friend who should be joining me.</p>
    <p class="terms-band">T.C Tag your posts to @brightloopsydney<br>to win points for the competition.</p>
  </main>
</body>
</html>
```